Now Leasing Banner

Looking for a banner that says the following information approx 4' x 30'

Now Leasing Maplewood Terrace 925-318-6054

Target Market(s)

Drive by traffic

Industry/Entity Type

Residential property management

Requirements
Must have
• Clear and readable from a distance

```html
<!DOCTYPE html>
<html lang="en">
<head>
<meta charset="UTF-8">
<title>Now Leasing Maplewood Terrace</title>
<link href="https://fonts.googleapis.com/css2?family=Poppins:wght@700;800&display=swap" rel="stylesheet">
<style>
  :root {
    --page: #ffffff;
    --navy: #14244a;
    --white: #ffffff;
    --ink: #111111;
    --stucco: #c9b79c;
    --sky: #a9c4e4;
    --hex-edge: #ffffff;
    --room-warm: #b89c80;
    --room-soft: #d9cfc3;
    --aerial: #7d8f6a;
  }
  * { margin: 0; padding: 0; box-sizing: border-box; }
  html, body {
    width: 1200px;
    height: 211px;
    overflow: hidden;
    background: var(--page);
  }
  .banner {
    position: absolute;
    left: 56px;
    top: 27px;
    width: 1112px;
    height: 153px;
    background: var(--navy);
    overflow: hidden;
  }
  .building-photo {
    position: absolute;
    left: 0;
    top: 0;
    width: 330px;
    height: 153px;
    background: linear-gradient(180deg, var(--sky) 0%, var(--stucco) 28%, #b8a388 70%, #8e8a74 100%);
  }
  .gallery {
    position: absolute;
    left: 0;
    top: 0;
    width: 1112px;
    height: 153px;
  }
  .headline {
    position: absolute;
    left: 430px;
    top: 10px;
    width: 620px;
    text-align: center;
    font-family: "Poppins", sans-serif;
    font-weight: 700;
    font-size: 33px;
    line-height: 48px;
    color: var(--white);
    letter-spacing: 0.2px;
  }
  .phone-strip {
    position: absolute;
    left: 0;
    top: 0;
    width: 1112px;
    height: 153px;
  }
  .phone-number {
    position: absolute;
    left: 575px;
    top: 72px;
    width: 430px;
    height: 56px;
    display: flex;
    align-items: center;
    justify-content: center;
    gap: 16px;
    font-family: "Poppins", sans-serif;
    font-weight: 800;
    font-size: 38px;
    color: var(--ink);
  }
  .phone-icon { width: 36px; height: 36px; flex: none; }
</style>
</head>
<body>
  <div class="banner">
    <div class="building-photo" role="img" aria-label="Photo of the apartment building exterior with balconies"></div>

    <svg class="gallery" viewBox="0 0 1112 153">
      <g stroke="var(--hex-edge)" stroke-width="4">
        <polygon role="img" aria-label="Photo of a furnished living room" fill="var(--room-soft)"
          points="278,34 295,5 329,5 346,34 329,63 295,63"/>
        <polygon role="img" aria-label="Photo of a bright interior room" fill="var(--room-warm)"
          points="328,46 345,17 379,17 396,46 379,75 345,75"/>
        <polygon role="img" aria-label="Photo of a living room with fireplace" fill="#a58a70"
          points="278,100 295,71 329,71 346,100 329,129 295,129"/>
        <polygon role="img" aria-label="Aerial photo of the apartment community" fill="var(--aerial)"
          points="330,120 347,91 381,91 398,120 381,149 347,149"/>
      </g>
    </svg>

    <h1 class="headline">Now Leasing Maplewood Terrace</h1>

    <svg class="phone-strip" viewBox="0 0 1112 153" aria-hidden="true">
      <polygon fill="var(--white)" points="496,71 1000,71 1020,128 516,128"/>
    </svg>

    <div class="phone-number">
      <svg class="phone-icon" viewBox="0 0 24 24" aria-hidden="true">
        <path fill="var(--ink)" d="M6.6 10.8a15.1 15.1 0 0 0 6.6 6.6l2.2-2.2a1 1 0 0 1 1-.25 11.4 11.4 0 0 0 3.6.57 1 1 0 0 1 1 1V20a1 1 0 0 1-1 1A17 17 0 0 1 3 4a1 1 0 0 1 1-1h3.5a1 1 0 0 1 1 1c0 1.25.2 2.45.57 3.57a1 1 0 0 1-.25 1z"/>
        <path fill="none" stroke="var(--ink)" stroke-width="1.8" stroke-linecap="round" d="M14 2.5a7.5 7.5 0 0 1 7.5 7.5M14 6a4 4 0 0 1 4 4"/>
      </svg>
      <span>925-318-6054</span>
    </div>
  </div>
</body>
</html>
```